GUARANTEED! Simple website for independent event planner and consultant...

I need a website that is no more than 5 or 6 pages to illustrate who I am and what I can offer to groups who book hotels for meetings and conferences. I have 20 years of experience planning meetings within hotels and I am now ready to go out on my own and help clients choose venues, negotiate contracts and plan effective meetings. I will focus on clients planning meetings in the mountains of Colorado but I am willing to travel as well. I want to work with a person who is collaborative and can direct me on what they need to move the project along quickly. I already have my logo, a hosting site and work e-mail address. Also, I recently hired a photographer to do head shots. Lastly, it important for me to be able to talk on the phone or skype with this person, as needed and I must be able to make changes to my site down the road when necessary...

Target Market(s)

Corporate Groups

Industry/Entity Type

Event Planning

Coding

Coded - Design and coding required

Number of Pages Required

5+ page

Font styles to use
Sans Serif

Requirements
Must have
• About me page, event planning services offered page, task force and consulting work page, testimonials page, page for blogs, page to contact me/request a proposal. May need advice on what else I need...
Nice to have
• I want it to look sharp and professional. I want people to look at my site and know immediately that they can trust me and the work I can do.
• I don't want it to look like it is over the top as I am not a HUGE company but I do want it to be professional and easy to view and navigate.
Should not have
• Bright colors
• My logo is bright orange and black. I have also used dark grey and orange. See below:
• Orange:
• C = 0
• M = 64
• Y = 100
• K = 0
• Gray:
• C = 67
• M = 60
• Y = 59
• K = 45
• Font: Gotham Book and Gotham Bold

```html
<!DOCTYPE html>
<html lang="en">
<head>
<meta charset="utf-8">
<title>Harlow Event Planning</title>
<link href="https://fonts.googleapis.com/css2?family=Montserrat:wght@400;500;600;700&display=swap" rel="stylesheet">
<style>
:root{
  --orange:#f47920;
  --charcoal:#3a3a3c;
  --ink:#2b2b2b;
  --text:#6b6b6b;
  --muted:#9a9a9a;
  --light:#f3f3f3;
  --line:#e4e4e4;
  --white:#ffffff;
  --footer:#333335;
}
*{box-sizing:border-box;margin:0;padding:0}
html,body{width:1200px;height:3133px;overflow:hidden}
body{font-family:'Montserrat',Arial,sans-serif;color:var(--text);background:var(--white);position:relative}
.wrap{width:980px;margin:0 auto;position:relative}
p{font-size:13px;line-height:22px}
.section-title{font-size:28px;font-weight:500;color:var(--ink);text-align:center}
.section-intro{width:760px;margin:16px auto 0;text-align:center;font-size:12.5px;line-height:21px;color:var(--text)}
.btn{display:inline-block;background:var(--orange);color:var(--white);font-size:12px;font-weight:600;letter-spacing:.5px;text-transform:uppercase}

/* Hero */
.hero{position:absolute;left:0;top:0;width:1200px;height:600px}
.hero-photo{position:absolute;inset:0;background:linear-gradient(180deg,#2a2622 0%,#4a423a 35%,#6a6158 60%,#3b3631 100%)}
.hero-shade{position:absolute;inset:0;background:rgba(20,18,16,.45)}
.nav{position:absolute;top:38px;left:110px;width:980px;height:64px;display:flex;align-items:center}
.brand{display:flex;align-items:center;gap:12px;color:var(--white);font-weight:600;font-size:15px;letter-spacing:1px;line-height:18px;text-transform:uppercase}
.brand-mark{width:18px;height:18px;background:var(--orange)}
.nav-links{display:flex;gap:38px;margin-left:auto;margin-right:46px;list-style:none}
.nav-links li{color:var(--white);font-size:12px;font-weight:500;letter-spacing:.5px;text-transform:uppercase}
.search{width:36px;height:36px;background:var(--orange);display:flex;align-items:center;justify-content:center}
.hero-copy{position:absolute;top:200px;left:0;width:1200px;text-align:center;color:var(--white)}
.hero-copy h1{font-size:34px;font-weight:700;letter-spacing:1px;text-transform:uppercase}
.hero-copy p{font-size:20px;line-height:30px;margin:22px auto 0;width:820px;font-weight:400}
.hero-copy .btn{margin-top:42px;padding:22px 40px;font-size:14px}

/* Services */
.services{position:absolute;top:600px;left:0;width:1200px;height:283px}
.service-list{display:flex;justify-content:space-between;width:900px;margin:52px auto 0}
.service{width:200px;text-align:center}
.service-icon{width:48px;height:48px;margin:0 auto}
.service h3{font-size:14px;font-weight:600;color:var(--ink);margin-top:18px;text-transform:uppercase}
.service p{font-size:12px;line-height:19px;margin-top:10px}

/* About */
.about{position:absolute;top:883px;left:0;width:1200px;height:345px;background:var(--light)}
.about h2{position:absolute;top:40px;left:110px;font-size:28px;font-weight:500;color:var(--ink)}
.about p{position:absolute;top:94px;left:110px;width:580px;font-size:12px;line-height:20px}
.about .btn{position:absolute;top:232px;left:110px;padding:15px 20px}
.about-photo{position:absolute;top:0;left:736px;width:345px;height:345px;background:linear-gradient(160deg,#e9e9e9 0%,#cfcfcf 60%,#9b9b9b 100%)}

/* Blog */
.blog{position:absolute;top:1228px;left:0;width:1200px;height:605px}
.blog .section-title{margin-top:46px}
.blog-cards{display:flex;justify-content:space-between;width:980px;margin:40px auto 0}
.card{width:310px;height:378px;background:var(--white);box-shadow:0 1px 6px rgba(0,0,0,.12)}
.card-photo{height:216px}
.card-body{padding:16px 20px}
.card h4{font-size:13.5px;font-weight:600;color:var(--ink)}
.card-meta{display:flex;gap:26px;margin-top:12px;font-size:10.5px;color:var(--muted)}
.card-meta span{display:flex;align-items:center;gap:6px}
.dot{width:8px;height:8px;border-radius:50%;background:var(--muted)}
.card-author{display:flex;align-items:center;gap:10px;border-top:1px solid var(--line);margin-top:18px;padding-top:16px;font-size:12px;color:var(--ink)}
.avatar{width:26px;height:26px;border-radius:50%;background:#c9c9c9}

/* Testimonials */
.testimonials{position:absolute;top:1833px;left:0;width:1200px;height:329px;background:var(--light)}
.testimonials .section-title{margin-top:40px}
.quote-list{display:flex;justify-content:space-between;width:980px;margin:30px auto 0}
.quote{width:470px;height:146px;background:var(--white);display:flex;padding:22px 26px;gap:26px}
.quote-photo{width:100px;height:100px;background:#d6d6d6;flex:none}
.quote p{font-size:12px;line-height:19px}
.quote .name{margin-top:10px;color:var(--orange);font-size:12px}

/* Contact */
.contact{position:absolute;top:2162px;left:0;width:1200px;height:538px}
.contact-photo{position:absolute;inset:0;background:linear-gradient(100deg,#2a2a2b 0%,#3a3836 45%,#5d5852 75%,#7a736b 100%)}
.contact-shade{position:absolute;inset:0;background:rgba(25,25,26,.55)}
.contact-inner{position:absolute;top:40px;left:110px;width:470px;color:var(--white)}
.contact h2{font-size:28px;font-weight:500}
.contact p{font-size:12px;line-height:19px;margin-top:14px;color:#d8d8d8}
.field{height:44px;background:#ededed;margin-top:9px;font-size:11px;color:var(--muted);padding:14px 12px}
.field:first-of-type{margin-top:22px}
.field.message{height:84px}
.contact .btn{margin-top:36px;padding:15px 18px}

/* Newsletter */
.newsletter{position:absolute;top:2700px;left:0;width:1200px;height:245px;text-align:center}
.newsletter .section-title{margin-top:44px}
.signup{display:flex;width:480px;margin:20px auto 0}
.signup-input{flex:1;height:42px;background:#ececec;text-align:left;padding:14px;font-size:11px;color:var(--muted)}
.signup-btn{width:50px;height:42px;background:var(--orange);display:flex;align-items:center;justify-content:center}

/* Footer */
.footer{position:absolute;top:2945px;left:0;width:1200px;height:188px;background:var(--footer)}
.footer-links{position:absolute;top:70px;left:110px;display:flex;gap:32px;list-style:none}
.footer-links li{color:var(--white);font-size:12px;font-weight:500;text-transform:uppercase}
.footer .brand{position:absolute;top:55px;right:110px;color:var(--orange)}
.footer .brand-mark{background:var(--orange)}
.copyright{position:absolute;top:150px;left:110px;font-size:11px;color:#8d8d8d}
.social{position:absolute;top:142px;right:110px;display:flex;gap:10px}
.social span{width:26px;height:26px;border-radius:50%;border:1px solid #8d8d8d}
</style>
</head>
<body>

<header class="hero">
  <div class="hero-photo" role="img" aria-label="Conference room with rows of chairs and tables"></div>
  <div class="hero-shade"></div>
  <nav class="nav">
    <div class="brand"><span class="brand-mark"></span><span>Harlow<br>Event Planning</span></div>
    <ul class="nav-links">
      <li>About</li><li>Services</li><li>Task Force</li><li>Consulting</li><li>Testimonial</li><li>Blog</li><li>Contact</li>
    </ul>
    <div class="search">
      <svg width="16" height="16" viewBox="0 0 16 16"><circle cx="6.5" cy="6.5" r="4.8" fill="none" stroke="#fff" stroke-width="2"/><line x1="10" y1="10" x2="14.5" y2="14.5" stroke="#fff" stroke-width="2.2"/></svg>
    </div>
  </nav>
  <div class="hero-copy">
    <h1>20 Years of Experience Planning Meetings</h1>
    <p>Industry's standard dummy text ever since the 1500s, when an unknown printer took a galley of type and scrambled it to make a type specimen book. It has survived not only five centuries.</p>
    <span class="btn">Request a Proposal</span>
  </div>
</header>

<section class="services">
  <div class="service-list">
    <div class="service">
      <svg class="service-icon" viewBox="0 0 48 48"><rect width="48" height="48" rx="6" fill="var(--orange)"/><circle cx="24" cy="16" r="5" fill="#fff"/><circle cx="13" cy="22" r="4" fill="#fff"/><circle cx="35" cy="22" r="4" fill="#fff"/><rect x="18" y="24" width="12" height="14" rx="3" fill="#fff"/></svg>
      <h3>Meeting Planning</h3>
      <p>Industry's standard dummy text ever since the 1500s, when an unknown printer.</p>
    </div>
    <div class="service">
      <svg class="service-icon" viewBox="0 0 48 48"><rect width="48" height="48" rx="6" fill="var(--orange)"/><circle cx="24" cy="12" r="4" fill="#fff"/><rect x="20" y="18" width="8" height="8" fill="#fff"/><rect x="14" y="27" width="20" height="13" fill="#fff"/></svg>
      <h3>Conference</h3>
      <p>Industry's standard dummy text ever since the 1500s, when an unknown printer.</p>
    </div>
    <div class="service">
      <svg class="service-icon" viewBox="0 0 48 48"><rect width="48" height="48" rx="6" fill="var(--orange)"/><rect x="13" y="10" width="22" height="28" fill="none" stroke="#fff" stroke-width="2.5"/><line x1="18" y1="18" x2="30" y2="18" stroke="#fff" stroke-width="2"/><line x1="18" y1="24" x2="30" y2="24" stroke="#fff" stroke-width="2"/><line x1="18" y1="30" x2="26" y2="30" stroke="#fff" stroke-width="2"/></svg>
      <h3>Event Logistics</h3>
      <p>Industry's standard dummy text ever since the 1500s, when an unknown printer.</p>
    </div>
    <div class="service">
      <svg class="service-icon" viewBox="0 0 48 48"><rect width="48" height="48" rx="6" fill="var(--orange)"/><rect x="11" y="12" width="26" height="18" fill="none" stroke="#fff" stroke-width="2.5"/><line x1="24" y1="30" x2="24" y2="38" stroke="#fff" stroke-width="2.5"/><line x1="17" y1="38" x2="31" y2="38" stroke="#fff" stroke-width="2.5"/></svg>
      <h3>Trade Show</h3>
      <p>Industry's standard dummy text ever since the 1500s, when an unknown printer.</p>
    </div>
  </div>
</section>

<section class="about">
  <h2>About me</h2>
  <p>It is a long established fact that a reader will be distracted by the readable content of a page when looking at its layout. The point of using Lorem Ipsum is that it has a more-or-less normal distribution of letters, as opposed to using content here, content here, making it look like readable English. Many desktop publishing packages and web page editors now use Lorem Ipsum as their default model text, and a search will uncover many web sites still in their infancy. Various versions have evolved over the years, sometimes by accident.</p>
  <span class="btn">Know More</span>
  <div class="about-photo" role="img" aria-label="Head shot of the event planner"></div>
</section>

<section class="blog">
  <h2 class="section-title">Latest Blog</h2>
  <p class="section-intro">It is a long established fact that a reader will be distracted by the readable content of a page when looking at its layout. The point of using Lorem Ipsum is that it has a more-or-less normal distribution of letters, as opposed to using content here, making it look like readable English.</p>
  <div class="blog-cards">
    <article class="card">
      <div class="card-photo" role="img" aria-label="Meeting room set with a laptop on the table" style="background:linear-gradient(160deg,#5c5f63,#2f3236)"></div>
      <div class="card-body">
        <h4>Provide point of using Lorem Ipsum</h4>
        <div class="card-meta"><span><i class="dot"></i>08 July, 2017</span><span><i class="dot"></i>1523 People Like</span></div>
        <div class="card-author"><span class="avatar"></span>Using Lorem Ipsum</div>
      </div>
    </article>
    <article class="card">
      <div class="card-photo" role="img" aria-label="Speaker in a suit presenting at a conference hall" style="background:linear-gradient(160deg,#d9a25c,#a86a3a 55%,#5a6e8a)"></div>
      <div class="card-body">
        <h4>Provide point of using Lorem Ipsum</h4>
        <div class="card-meta"><span><i class="dot"></i>08 July, 2017</span><span><i class="dot"></i>1523 People Like</span></div>
        <div class="card-author"><span class="avatar"></span>Using Lorem Ipsum</div>
      </div>
    </article>
    <article class="card">
      <div class="card-photo" role="img" aria-label="Colleagues in a meeting around a screen" style="background:linear-gradient(160deg,#dde2e6,#a9b3bb 60%,#7b8690)"></div>
      <div class="card-body">
        <h4>Provide point of using Lorem Ipsum</h4>
        <div class="card-meta"><span><i class="dot"></i>08 July, 2017</span><span><i class="dot"></i>1523 People Like</span></div>
        <div class="card-author"><span class="avatar"></span>Using Lorem Ipsum</div>
      </div>
    </article>
  </div>
</section>

<section class="testimonials">
  <h2 class="section-title">Testimonials</h2>
  <p class="section-intro">It is a long established fact that a reader will be distracted by the readable content of a page when looking at its layout. The point of using Lorem Ipsum is that it has a more-or-less normal distribution.</p>
  <div class="quote-list">
    <div class="quote">
      <div class="quote-photo" role="img" aria-label="Client portrait placeholder"></div>
      <div><p>It is a long established fact that a reader will be distracted by the readable content of a page when looking at its layout. The point of using Lorem Ipsum has a more-or-less.</p><p class="name">Mr. Client Name</p></div>
    </div>
    <div class="quote">
      <div class="quote-photo" role="img" aria-label="Client portrait placeholder"></div>
      <div><p>It is a long established fact that a reader will be distracted by the readable content of a page when looking at its layout. The point of using Lorem Ipsum has a more-or-less.</p><p class="name">Mr. Client Name</p></div>
    </div>
  </div>
</section>

<section class="contact">
  <div class="contact-photo" role="img" aria-label="Hands typing on a laptop keyboard"></div>
  <div class="contact-shade"></div>
  <div class="contact-inner">
    <h2>Get in Touch</h2>
    <p>It is a long established fact that a reader will be distracted by the readable content of a page when looking at its layout. The point of using Lorem Ipsum has a more-or-less normal distribution.</p>
    <div class="field">First Name</div>
    <div class="field">Last Name</div>
    <div class="field">Email</div>
    <div class="field message">Message</div>
    <span class="btn">Let's Go</span>
  </div>
</section>

<section class="newsletter">
  <h2 class="section-title">Newsletter Sign Up</h2>
  <p class="section-intro">It is a long established fact that a reader will be distracted by the readable content of a page when looking at its layout. The point of using Lorem Ipsum is that it has a more-or-less normal distribution.</p>
  <div class="signup">
    <div class="signup-input">Email</div>
    <div class="signup-btn"><svg width="16" height="16" viewBox="0 0 16 16"><path d="M1 1 L15 8 L1 15 L4 8 Z" fill="#fff"/></svg></div>
  </div>
</section>

<footer class="footer">
  <ul class="footer-links">
    <li>About</li><li>Services</li><li>Task Force</li><li>Consulting</li><li>Testimonial</li><li>Blog</li><li>Contact</li>
  </ul>
  <div class="brand"><span class="brand-mark"></span><span>Harlow<br>Event Planning</span></div>
  <p class="copyright">All Rights Reserved</p>
  <div class="social"><span></span><span></span><span></span></div>
</footer>

</body>
</html>
```